Breakthrough book for CEO's for navigating exponential change (very timely!)

This book changes the way leaders approach change. It comes from deep experience - seeing first hand what isn't working. It will be a book still being purchased in 5 or 10 years time, and broadly quoted. The author is female, doesn't want to shown up as "look at me" (the work is the hero) but needs to command authority among C-Suite which skews strongly male. The book is about systems thinking, hence why I've been exploring designs that cue "systems" (attached). It would be good to keep exploring this theme, along with others. Attached are files which give more background: including author / brand guidelines, a design brief, Bring your creativity and energy - and help me connect and cut through to the people who really need this book!

Target Market(s)

CEO's, Senior Executive Leaders

Industry/Entity Type

Business, Corporate

Font styles to use
Other font styles liked:
• See the brief: Raleway and Beyond Infinity

Colors

Designer to choose colors to be used in the design.

Requirements
Must have
• Implicit authority and deep insight. This is a book that says there is depth beyond the cover
Nice to have
• See the brief
Should not have
• the usual arrows, bridges and a shouting style.

```html
<!DOCTYPE html>
<html lang="en">
<head>
<meta charset="utf-8">
<title>Guiding Swift Realignment – Book Cover</title>
<link rel="stylesheet" href="https://fonts.googleapis.com/css2?family=Cormorant+Garamond:wght@600&family=Libre+Baskerville&family=Cinzel:wght@500&family=Raleway:wght@500&display=swap">
<style>
  :root {
    --page: #ffffff;
    --crimson: #8a0f2c;
    --crimson-deep: #4e0a1e;
    --night: #1f1530;
    --cream: #f6e9c4;
    --gold: #d9a85c;
    --gold-light: #f3d08a;
    --rose: #b5606e;
    --teal: #2a5660;
  }
  html, body {
    margin: 0;
    width: 1200px;
    height: 1200px;
    overflow: hidden;
    background: var(--page);
  }
  .canvas {
    position: relative;
    width: 1200px;
    height: 1200px;
  }
  .book-cover {
    position: absolute;
    left: 222px;
    top: 32px;
    width: 762px;
    height: 1144px;
    display: block;
  }
  .title-line {
    font-family: "Cormorant Garamond", Georgia, serif;
    font-weight: 600;
    font-size: 90px;
    fill: var(--cream);
    text-anchor: middle;
  }
  .subtitle {
    font-family: "Libre Baskerville", Georgia, serif;
    font-size: 40px;
    fill: var(--cream);
    text-anchor: middle;
  }
  .series-line {
    font-family: "Libre Baskerville", Georgia, serif;
    font-size: 18px;
    fill: var(--cream);
    text-anchor: middle;
  }
  .author-name {
    font-family: "Cinzel", "Times New Roman", serif;
    font-weight: 500;
    font-size: 50px;
    letter-spacing: 2px;
    fill: var(--cream);
    text-anchor: middle;
  }
  .author-role {
    font-family: "Raleway", Arial, sans-serif;
    font-weight: 500;
    font-size: 15px;
    letter-spacing: 5.2px;
    fill: var(--cream);
    text-anchor: middle;
  }
</style>
</head>
<body>
<main class="canvas">
  <svg class="book-cover" viewBox="0 0 762 1144" xmlns="http://www.w3.org/2000/svg">
    <defs>
      <radialGradient id="cover-bg" cx="0.5" cy="0.22" r="0.85">
        <stop offset="0" stop-color="var(--crimson)"/>
        <stop offset="0.6" stop-color="#6a0c24"/>
        <stop offset="1" stop-color="var(--crimson-deep)"/>
      </radialGradient>
      <linearGradient id="night-fade" x1="0" y1="0" x2="0" y2="1">
        <stop offset="0" stop-color="#241330"/>
        <stop offset="1" stop-color="#2d0f26"/>
      </linearGradient>
      <radialGradient id="network-glow" cx="0.62" cy="0.55" r="0.6">
        <stop offset="0" stop-color="#fff2c4"/>
        <stop offset="0.18" stop-color="#e2a451"/>
        <stop offset="0.5" stop-color="#2b1a2c"/>
        <stop offset="0.8" stop-color="#5a0f26" stop-opacity="0.6"/>
        <stop offset="1" stop-color="#6a0c24" stop-opacity="0"/>
      </radialGradient>
      <linearGradient id="ribbon-gold" x1="0" y1="0" x2="1" y2="0">
        <stop offset="0" stop-color="#c9a26a"/>
        <stop offset="0.5" stop-color="var(--gold-light)"/>
        <stop offset="1" stop-color="var(--gold)"/>
      </linearGradient>
    </defs>

    <rect class="cover-background" width="762" height="1144" fill="url(#cover-bg)"/>

    <g class="cover-title">
      <text class="title-line" x="381" y="102">GUIDING</text>
      <text class="title-line" x="381" y="176">SWIFT</text>
      <text class="title-line" x="381" y="249">REALIGNMENT</text>
    </g>

    <ellipse class="network-globe" cx="381" cy="470" rx="300" ry="215" fill="url(#network-glow)"
             role="img" aria-label="Glowing globe wrapped in a golden network of connected points and orbiting lines"/>

    <g class="lower-field">
      <path class="night-field" d="M0 975 C 180 930, 330 890, 466 850 S 680 775, 762 760 L 762 1144 L 0 1144 Z" fill="url(#night-fade)"/>
      <path class="ribbon-teal" d="M420 862 C 560 820, 650 740, 762 705 L 762 752 C 660 775, 560 830, 466 852 Z" fill="var(--teal)" opacity="0.9"/>
      <path class="ribbon-rose" d="M0 985 C 180 950, 330 900, 480 850 L 500 852 C 360 905, 200 985, 0 1030 Z" fill="var(--rose)" opacity="0.85"/>
      <path class="ribbon-gold" d="M0 952 C 180 920, 330 880, 466 840 S 680 760, 762 745 L 762 773 C 680 785, 560 830, 466 858 S 180 965, 0 993 Z" fill="url(#ribbon-gold)"/>
    </g>

    <g class="subtitle-seal">
      <circle cx="381" cy="746" r="155" fill="var(--night)"/>
      <circle cx="381" cy="746" r="155" fill="none" stroke="var(--gold)" stroke-width="2.5"/>
      <circle cx="381" cy="746" r="148" fill="none" stroke="var(--gold)" stroke-width="1" opacity="0.6"/>
      <text class="subtitle" x="381" y="705">Growth</text>
      <text class="subtitle" x="381" y="748">beyond</text>
      <text class="subtitle" x="381" y="792">upheaval</text>
      <text class="series-line" x="381" y="818">The Adaptive Leader Guide</text>
    </g>

    <g class="author-block">
      <text class="author-name" x="381" y="1059">Helena Ashcroft</text>
      <line x1="131" y1="1068" x2="631" y2="1068" stroke="var(--cream)" stroke-width="1"/>
      <text class="author-role" x="381" y="1092">BUSINESS LEADERSHIP &amp; CHANGE EXPERT</text>
    </g>
  </svg>
</main>
</body>
</html>
```